International Honeymoon Tour Operator needs Business Card

We need to design a business card including our new logo for a new tour operator called Marisol Thorne Getaways. We would like to also include the text 'Personal Tailor-Made Honeymoons for our Guests at a Lower Cost'. Please Include the following details as well; 'Website: www.marisolthornegetaways.co.uk'; 'E-mail: felix@marisolthornegetaways.co.uk'; 'Mobile: 07914263058'. We would like the design to be compatible with the logo and text. The final design should communicate professionalism, modern and ethical.

We want to business card to be double sided.

We would like to be able to easily adjust the e-mail address and contact number in the future for other employees either through you or ourselves.

Target Market(s)

Brides and grooms aged 18-35 predominantly.

Industry/Entity Type

Business

Colors

Designer to choose colors to be used in the design.

Requirements
Must have
• Logo
Requested Text
Double sided
Nice to have
• Additional colour
The wow factor
Should not have
• Images of currency

```html
<!DOCTYPE html>
<html lang="en">
<head>
<meta charset="utf-8">
<title>Marisol Thorne Getaways – Business Card</title>
<link href="https://fonts.googleapis.com/css2?family=Abel&display=swap" rel="stylesheet">
<style>
  :root {
    --backdrop: #e9e4dd;
    --card: #ffffff;
    --frame-dark: #5b5b5e;
    --frame-light: #c9c9cc;
    --band: #58493f;
    --band-text: #ffffff;
    --brand: #3f8d9b;
    --brand-dot: #8cc63f;
    --text: #4a4a4a;
    --icon-bg: #3d3d3f;
    --rule: #9a9a9a;
  }
  * { margin: 0; padding: 0; box-sizing: border-box; }
  html, body {
    width: 1200px; height: 677px; overflow: hidden;
    background: var(--backdrop);
    font-family: "Abel", sans-serif;
  }
  .stage {
    width: 1200px; height: 677px;
    display: flex; justify-content: center; align-items: center; gap: 60px;
  }
  .card {
    position: relative;
    width: 340px; height: 590px;
    padding: 8px;
    background: linear-gradient(135deg, var(--frame-dark), var(--frame-light) 45%, var(--frame-dark) 70%, var(--frame-light));
    box-shadow: 0 10px 30px rgba(0,0,0,.18);
  }
  .card-face {
    position: relative;
    width: 100%; height: 100%;
    background: var(--card);
  }
  .brand {
    position: absolute; top: 95px; left: 0; right: 0;
    display: flex; flex-direction: column; align-items: center; gap: 12px;
  }
  .brand-dot {
    width: 34px; height: 34px; border-radius: 50%;
    background: var(--brand-dot);
  }
  .brand-name {
    color: var(--brand);
    font-size: 25px; letter-spacing: 1px;
    text-align: center; line-height: 1.15;
  }
  .name-band {
    position: absolute; top: 250px; left: 0; right: 0;
    height: 84px;
    background: var(--band);
    color: var(--band-text);
    text-align: center;
    display: flex; flex-direction: column; justify-content: center;
    letter-spacing: 2px;
  }
  .person-name { font-size: 25px; font-weight: 400; line-height: 1.1; }
  .person-role { font-size: 19px; line-height: 1.2; }
  .contacts {
    position: absolute; top: 356px; left: 22px; right: 14px;
    list-style: none;
  }
  .contact {
    display: flex; align-items: center; gap: 12px;
    height: 28px;
    color: var(--text); font-size: 14.5px;
    white-space: nowrap;
  }
  .contact-icon {
    flex: none;
    width: 19px; height: 19px;
    background: var(--icon-bg);
    display: flex; align-items: center; justify-content: center;
  }
  .contact-icon svg { width: 13px; height: 13px; fill: #fff; }
  .rule {
    position: absolute; left: 10px; right: 10px;
    height: 1px; background: var(--rule);
  }
  .rule-top { top: 480px; }
  .rule-bottom { top: 528px; }
  .address {
    position: absolute; top: 490px; left: 22px; right: 14px;
  }

  /* Reverse side */
  .back-brand {
    position: absolute; top: 170px; left: 0; right: 0;
    display: flex; flex-direction: column; align-items: center; gap: 14px;
  }
  .back-brand .brand-dot { width: 44px; height: 44px; }
  .back-brand .brand-name { font-size: 30px; }
  .tagline-band {
    position: absolute; top: 372px; left: 0; right: 0;
    height: 84px;
    padding: 0 28px;
    background: var(--band);
    color: var(--band-text);
    display: flex; align-items: center; justify-content: center;
    text-align: center;
    font-size: 17px; line-height: 1.35; letter-spacing: 1px;
  }
</style>
</head>
<body>
<main class="stage">
  <article class="card card-front">
    <div class="card-face">
      <div class="brand">
        <span class="brand-dot"></span>
        <span class="brand-name">Marisol Thorne<br>Getaways</span>
      </div>

      <header class="name-band">
        <h1 class="person-name">DORIAN VALE</h1>
        <p class="person-role">GENERAL MANAGER</p>
      </header>

      <ul class="contacts">
        <li class="contact">
          <span class="contact-icon"><svg viewBox="0 0 16 16"><path d="M3.5 1.5l2.5 2.5-1.5 2a8 8 0 0 0 5.5 5.5l2-1.5 2.5 2.5-2 2C7 14.5 1.5 9 1.5 3.5z"/></svg></span>
          07914263058
        </li>
        <li class="contact">
          <span class="contact-icon"><svg viewBox="0 0 16 16"><path d="M4.5 1h7v14h-7zM6 3v9h4V3zm1.5 10h1v1h-1z" fill-rule="evenodd"/></svg></span>
          01632 960418
        </li>
        <li class="contact">
          <span class="contact-icon"><svg viewBox="0 0 16 16"><path d="M1.5 3.5h13v9h-13zM2.5 4.5 8 9l5.5-4.5v1L8 10 2.5 5.5z" fill-rule="evenodd"/></svg></span>
          felix@marisolthornegetaways.co.uk
        </li>
        <li class="contact">
          <span class="contact-icon"><svg viewBox="0 0 16 16"><path d="M8 1.5a6.5 6.5 0 1 0 0 13 6.5 6.5 0 0 0 0-13zm0 1.2c1 1 1.6 2.9 1.7 4.7H6.3C6.4 5.6 7 3.7 8 2.7zM6.3 8.6h3.4c-.1 1.8-.7 3.7-1.7 4.7-1-1-1.6-2.9-1.7-4.7zM2.8 7.4a5.300 5.300 0 0 1 2.6-4c-.5 1.1-.9 2.5-1 4zm0 1.2h1.6c.1 1.5.5 2.9 1 4a5.3 5.3 0 0 1-2.6-4zm10.4 0a5.3 5.3 0 0 1-2.6 4c.5-1.1.9-2.5 1-4zm0-1.2h-1.6c-.1-1.5-.5-2.9-1-4a5.3 5.3 0 0 1 2.6 4z"/></svg></span>
          www.marisolthornegetaways.co.uk
        </li>
      </ul>

      <span class="rule rule-top"></span>
      <p class="address contact">
        <span class="contact-icon"><svg viewBox="0 0 16 16"><path d="M8 1a4.5 4.5 0 0 0-4.5 4.5C3.5 9 8 15 8 15s4.5-6 4.5-9.5A4.5 4.5 0 0 0 8 1zm0 2.8a1.7 1.7 0 1 1 0 3.4 1.7 1.7 0 0 1 0-3.4z"/></svg></span>
        27 Harbour Lane, Kestrel Quay
      </p>
      <span class="rule rule-bottom"></span>
    </div>
  </article>

  <article class="card card-back">
    <div class="card-face">
      <div class="back-brand">
        <span class="brand-dot"></span>
        <span class="brand-name">Marisol Thorne<br>Getaways</span>
      </div>
      <p class="tagline-band">Personal Tailor-Made Honeymoons<br>for our Guests at a Lower Cost</p>
    </div>
  </article>
</main>
</body>
</html>
```